Modern Real Estate Sign For Realtor

We need to real estate sign 24x36 or (24x30 if it fits better) Sign that will be attached to a post at homes that are for sale. I like the style of the Harbor 47 yard signs I attached and PT sign with the white trim around it. I Also attached my business card with my logo and name. I would like a black sign with white writing.  I would also like to see options with my headshot included on the sign, either centered or on the right side. The following text should go on the sign:
Logo at the top.
Marcus Dunne
555.231.9067
Marcus@MDunneHomes.example

Requirements
Must have
- Logo at the top.
- Marcus Dunne
- 555.231.9067
- Marcus@MDunneHomes.example

Nice to have
- Headshot open to different design options for how it will be placed on the sign.
- MDunneHomes.example

```html
<!DOCTYPE html>
<html lang="en">
<head>
<meta charset="utf-8">
<title>MDunne Homes – Yard Sign</title>
<link rel="stylesheet" href="https://fonts.googleapis.com/css2?family=Raleway:wght@400;500&display=swap">
<style>
  :root {
    --page: #ffffff;
    --sign: #000000;
    --ink: #ffffff;
    --band: #bfb08a;
    --band-ink: #111111;
    --photo-a: #6f7d58;
    --photo-b: #3a3a3c;
  }
  html, body {
    margin: 0;
    padding: 0;
    width: 1200px;
    height: 999px;
    overflow: hidden;
    background: var(--page);
    font-family: "Raleway", sans-serif;
  }
  .canvas { position: relative; width: 1200px; height: 999px; }
  .sign {
    position: absolute; left: 236px; top: 44px;
    width: 729px; height: 909px;
    background: var(--sign);
  }
  .post-rule {
    position: absolute; left: 289px; top: 63px;
    width: 7px; height: 872px; background: var(--ink);
  }
  .arm-rule {
    position: absolute; left: 259px; top: 218px;
    width: 490px; height: 7px; background: var(--ink);
  }
  .brand {
    position: absolute; left: 336px; top: 146px; width: 378px;
    color: var(--ink);
    font-weight: 400; font-size: 38px; letter-spacing: 3px;
    text-align: center; white-space: nowrap; line-height: 1;
  }
  .brand-underline {
    position: absolute; left: 355px; top: 192px;
    width: 350px; height: 1px; background: var(--ink);
  }
  .headshot {
    position: absolute; left: 736px; top: 136px;
    width: 200px; height: 200px; border-radius: 50%;
    border: 7px solid var(--ink);
    background: radial-gradient(circle at 50% 40%, var(--photo-a) 0%, #59624a 45%, var(--photo-b) 100%);
  }
  .agent-name {
    position: absolute; left: 344px; top: 532px;
    color: var(--ink); font-weight: 500; font-size: 38px;
    letter-spacing: 1px; line-height: 1; white-space: nowrap;
  }
  .agent-phone {
    position: absolute; left: 340px; top: 588px;
    color: var(--ink); font-weight: 400; font-size: 93px;
    line-height: 1; white-space: nowrap;
    font-variant-numeric: lining-nums;
  }
  .contact-band {
    position: absolute; left: 236px; top: 748px;
    width: 729px; height: 74px; background: var(--band);
  }
  .contact {
    position: absolute; top: 761px; height: 48px;
    display: flex; align-items: center; gap: 8px;
    color: var(--band-ink); font-weight: 500; font-size: 16px;
    white-space: nowrap;
  }
  .contact--email { left: 348px; }
  .contact--web { left: 682px; }
</style>
</head>
<body>
<div class="canvas">
  <div class="sign"></div>
  <div class="post-rule"></div>
  <div class="arm-rule"></div>

  <div class="brand">MDUNNE HOMES</div>
  <div class="brand-underline"></div>

  <div class="headshot" role="img" aria-label="Agent headshot photo"></div>

  <div class="agent-name">MARCUS DUNNE</div>
  <div class="agent-phone">555.231.9067</div>

  <div class="contact-band"></div>
  <div class="contact contact--email">
    <svg width="64" height="48" viewBox="0 0 64 48" aria-hidden="true">
      <rect x="2" y="4" width="60" height="40" fill="none" stroke="#111" stroke-width="3"/>
      <path d="M2 4 L32 28 L62 4 M2 44 L24 22 M62 44 L40 22" fill="none" stroke="#111" stroke-width="3"/>
      <text x="32" y="18" font-family="Raleway, sans-serif" font-size="14" font-weight="500" text-anchor="middle" fill="#111">@</text>
    </svg>
    <span>Marcus@MDunneHomes.example</span>
  </div>
  <div class="contact contact--web">
    <svg width="56" height="52" viewBox="0 0 56 52" aria-hidden="true">
      <g fill="none" stroke="#111" stroke-width="3">
        <circle cx="26" cy="25" r="22"/>
        <ellipse cx="26" cy="25" rx="10" ry="22"/>
        <line x1="26" y1="3" x2="26" y2="47"/>
        <line x1="4" y1="25" x2="48" y2="25"/>
        <path d="M8 13 H44 M8 37 H44"/>
      </g>
      <path d="M34 30 L52 44 L44 44 L48 51 L44 52 L40 46 L34 50 Z" fill="#111" stroke="#bfb08a" stroke-width="1.5"/>
    </svg>
    <span>MDunneHomes.example</span>
  </div>
</div>
</body>
</html>
```